Business Card design for a company called Tallow Flame NI

I need a business card design for my oil fired boiler servicing company. I have a logo design already and Im just looking that incorporated into the business card design. card details; Tallow Flame NI
Oil Burner Servicing - Mid Ulster Area
Service Engineer - Owen Marsh
Mobile 07751364927
email - Tallow.Flame.NI@hearthmail.example
www.tallowflameni.example
I carry out Servicing, Commissioning, Fault Finding, Warranty Validation
Target Market(s)
home owners with oil fired central heating
Industry/Entity Type
Business
Contact Information for Business Card
Tallow Flame NI
Tell. 07751364927
Web: www.tallowflameni.example
email Tallow.Flame.NI@Hearthmail.Example
Servicing Fault Finding Commissioning Warranty Validation
Look and feel

```html
<!DOCTYPE html>
<html lang="en">
<head>
<meta charset="utf-8">
<title>Tallow Flame NI — Business Card</title>
<link rel="stylesheet" href="https://fonts.googleapis.com/css2?family=Montserrat:wght@500;700;800&display=swap">
<style>
  :root {
    --backdrop: #3a3a3c;
    --card: #1f2225;
    --green: #4fc23a;
    --green-faint: rgba(79, 194, 58, 0.10);
    --icon-ink: #1f2225;
  }
  * { box-sizing: border-box; margin: 0; padding: 0; }
  html, body {
    width: 1200px;
    height: 1189px;
    overflow: hidden;
    background: var(--backdrop);
    font-family: "Montserrat", Arial, sans-serif;
    color: var(--green);
  }
  .canvas {
    position: relative;
    width: 1200px;
    height: 1189px;
  }
  .card {
    position: absolute;
    left: 150px;
    width: 900px;
    height: 510px;
    background: var(--card);
    border-radius: 26px;
    overflow: hidden;
    box-shadow: 0 18px 40px rgba(0, 0, 0, 0.45);
  }
  .card--services { top: 55px; }
  .card--contact { top: 624px; }

  /* Services side */
  .faint-circle {
    position: absolute;
    left: 260px;
    top: 40px;
    width: 430px;
    height: 430px;
    border-radius: 50%;
    background: var(--green-faint);
  }
  .services-brand {
    position: absolute;
    left: 190px;
    top: 150px;
    width: 600px;
  }
  .brand-name {
    font-weight: 800;
    font-size: 66px;
    line-height: 1;
    letter-spacing: 0.5px;
    color: var(--green);
    white-space: nowrap;
  }
  .brand-tagline {
    margin-top: 8px;
    font-weight: 500;
    font-size: 15px;
    letter-spacing: 3.4px;
    text-transform: uppercase;
    color: var(--green);
    white-space: nowrap;
  }
  .services-list {
    position: absolute;
    left: 140px;
    top: 318px;
    font-weight: 500;
    font-size: 24px;
    color: var(--green);
    white-space: nowrap;
  }
  .services-list .divider { padding: 0 3px; }

  /* Contact side */
  .brand-row {
    position: absolute;
    left: 60px;
    top: 70px;
    display: flex;
    align-items: center;
    gap: 26px;
  }
  .brand-dot {
    width: 150px;
    height: 150px;
    border-radius: 50%;
    background: var(--green);
    flex: none;
  }
  .brand-row .brand-name { font-size: 62px; }
  .brand-row .brand-tagline { font-size: 14px; letter-spacing: 3.2px; }

  .engineer {
    position: absolute;
    right: 60px;
    top: 232px;
    text-align: left;
  }
  .engineer-name {
    font-weight: 800;
    font-size: 30px;
    line-height: 1.05;
  }
  .engineer-role {
    font-weight: 700;
    font-size: 24px;
    line-height: 1.1;
  }
  .rule {
    position: absolute;
    left: 60px;
    top: 318px;
    width: 560px;
    height: 2px;
    background: var(--green);
  }
  .contact-list {
    position: absolute;
    left: 60px;
    bottom: 52px;
    list-style: none;
  }
  .contact-item {
    display: flex;
    align-items: center;
    gap: 16px;
    font-weight: 500;
    font-size: 26px;
    line-height: 1.35;
    white-space: nowrap;
  }
  .contact-icon {
    width: 30px;
    height: 30px;
    border-radius: 5px;
    background: var(--green);
    display: flex;
    align-items: center;
    justify-content: center;
    flex: none;
  }
  .web {
    position: absolute;
    right: 60px;
    top: 380px;
    font-weight: 500;
    font-size: 24px;
    white-space: nowrap;
  }
</style>
</head>
<body>
<main class="canvas">

  <section class="card card--services" aria-label="Card back: services">
    <div class="faint-circle" aria-hidden="true"></div>
    <div class="services-brand">
      <h1 class="brand-name">Tallow Flame NI</h1>
      <p class="brand-tagline">Oil Burner Servicing - Mid Ulster Area</p>
    </div>
    <p class="services-list">Servicing<span class="divider">|</span>Commissioning<span class="divider">|</span>Fault Finding<span class="divider">|</span>Warranty Validation</p>
  </section>

  <section class="card card--contact" aria-label="Card front: contact details">
    <div class="brand-row">
      <div class="brand-dot" aria-hidden="true"></div>
      <div>
        <h2 class="brand-name">Tallow Flame NI</h2>
        <p class="brand-tagline">Oil Burner Servicing - Mid Ulster Area</p>
      </div>
    </div>

    <div class="engineer">
      <p class="engineer-name">Owen Marsh</p>
      <p class="engineer-role">Service Engineer</p>
    </div>

    <div class="rule" aria-hidden="true"></div>

    <p class="web">www.tallowflameni.example</p>

    <ul class="contact-list">
      <li class="contact-item">
        <span class="contact-icon" aria-hidden="true">
          <svg width="20" height="20" viewBox="0 0 24 24">
            <path fill="var(--icon-ink)" d="M6.6 10.8a15.1 15.1 0 0 0 6.6 6.6l2.2-2.2a1 1 0 0 1 1-.25 11.4 11.4 0 0 0 3.6.57 1 1 0 0 1 1 1V20a1 1 0 0 1-1 1A17 17 0 0 1 3 4a1 1 0 0 1 1-1h3.5a1 1 0 0 1 1 1c0 1.25.2 2.45.57 3.57a1 1 0 0 1-.25 1z"/>
          </svg>
        </span>
        07751364927
      </li>
      <li class="contact-item">
        <span class="contact-icon" aria-hidden="true">
          <svg width="20" height="16" viewBox="0 0 20 16">
            <rect x="1" y="1" width="18" height="14" fill="none" stroke="var(--icon-ink)" stroke-width="2"/>
            <path d="M1 1l9 7 9-7" fill="none" stroke="var(--icon-ink)" stroke-width="2"/>
          </svg>
        </span>
        Tallow.Flame.NI@Hearthmail.Example
      </li>
    </ul>
  </section>

</main>
</body>
</html>
```